needing web design for aerial and satellite installation comapny

We need our website designing, it needs to be professional and look creative,
We are a aerial and satellite company called Kestrel Mend & Reach ()
I like this site design also some of the following maybe:

https://www.skywirelo.co.uk/

http://holdmoor.co.uk/

http://quillnine-guard.co.uk/portfolio/zmp-holdmoor/

The design will require coding once the design is complete, i haven't paid for this yet as i want to be sure the design is good before i commit.

The template needs to look professional and look like one of the leading companies.
The site will consist of all the features this site has https://www.skywirelo.co.uk/

I like a modern design with the latest technology.

Target Market(s)

tv aerial satellite installation

Industry/Entity Type

Satellite Tv

Number of Pages Required

3 page

Font styles to use
Sans Serif

Colors

Designer to choose colors to be used in the design.

Requirements
Must have
• eb Contest Brief We need our website designing, it needs to be professional and look creative,
• We are a aerial and satellite company called Kestrel Mend Reach ()
• I like this site design also some of the following maybe:
• https://www.skywirelo.co.uk/
• http://holdmoor.co.uk/
• http://quillnine-guard.co.uk/portfolio/zmp-holdmoor/
• The design will require coding once the design is complete, i haven't paid for this yet as i want to be sure the design is good before i commit.
• The template needs to look professional and look like one of the leading companies.
• The site will consist of all the features this site has https://www.skywirelo.co.uk/
• I like a modern design with the latest technology.
Nice to have
• http://holdmoor.co.uk/
Should not have
• poor design

```html
<!DOCTYPE html>
<html lang="en">
<head>
<meta charset="utf-8">
<title>Kestrel Mend &amp; Reach – Testimonials and Contact</title>
<link rel="stylesheet" href="https://fonts.googleapis.com/css2?family=Source+Sans+3:wght@400;600&family=PT+Sans+Narrow&family=Raleway:wght@300;400;500&display=swap">
<style>
:root{
  --navy:#1c2438;
  --orange:#f7941d;
  --ink:#333a45;
  --muted:#5e6470;
  --panel:#f6f7f9;
  --field:#ffffff;
  --footer-top:#13162e;
  --footer-text:#c9ccd6;
  --footer-dim:#8d93a6;
}
*{margin:0;padding:0;box-sizing:border-box}
html,body{width:1200px;height:1200px;overflow:hidden;background:#fff}
.canvas{position:relative;width:1200px;height:1200px;overflow:hidden;font-family:"Raleway",sans-serif;color:var(--ink)}
.abs{position:absolute}
h2,h3,h4{font-weight:400}

.hero-strip{left:0;top:0;width:1200px;height:42px;display:flex}
.hero-strip .left{width:596px;height:42px;background:linear-gradient(180deg,#1e3656,#2a4668)}
.hero-strip .right{flex:1;height:42px;background:linear-gradient(100deg,#e9ecef 0%,#9fb2c8 30%,#3a66a8 60%,#2f5fb0 100%)}

.testimonials{left:0;top:42px;width:1200px;height:364px;background:#fff}
.section-title{left:0;top:80px;width:1200px;text-align:center;font-family:"Source Sans 3",sans-serif;font-size:30px;font-weight:400;letter-spacing:1.8px;color:var(--navy)}
.section-title .accent{color:var(--orange)}
.quote-mark{left:580px;top:132px}
.quote-text{left:272px;top:172px;width:656px;text-align:center;font-family:"PT Sans Narrow",sans-serif;font-size:10.5px;line-height:24px;letter-spacing:.85px;color:#1f2430}

.avatar{width:84px;height:84px;border-radius:50%;border:2px solid #f2c58a;background:radial-gradient(circle at 50% 40%,#c9b8a8,#7d8590)}
.avatar.active{border-color:var(--orange);background:radial-gradient(circle at 50% 40%,#b59a86,#3d4a3f)}
.person{font-size:10px;line-height:16px;letter-spacing:.4px;color:var(--muted)}

.contact{left:0;top:406px;width:1200px;height:414px;background:var(--panel)}
.contact-title{left:0;top:436px;width:1252px;text-align:center;font-size:21px;letter-spacing:1px;color:#2e3340}
.info-head{left:296px;top:490px;font-size:15px;letter-spacing:.6px;color:#2e3340}
.info-body{font-size:10.4px;line-height:19.2px;letter-spacing:.6px;color:var(--muted)}
.info-label{font-size:10.4px;font-weight:500;letter-spacing:.4px;color:#222734}

.field{background:var(--field);font-size:8.5px;color:#a8adb7;padding:8px 12px;letter-spacing:.3px}
.send-btn{left:668px;top:731px;width:231px;height:34px;background:var(--orange);color:#fff;font-size:12px;font-weight:500;display:flex;align-items:center;justify-content:center;letter-spacing:.3px}

.footer-bar{left:0;top:820px;width:1200px;height:86px;background:var(--footer-top);border-top:4px solid #242a45}
.footer-text{font-size:10.4px;line-height:19px;letter-spacing:.3px;color:var(--footer-text)}
.social{width:18px;height:18px;border-radius:50%;background:#9096a6}

.footer-main{left:0;top:906px;width:1200px;height:294px;background:radial-gradient(ellipse at 40% 60%,#2c3557 0%,#1c2240 45%,#121629 100%)}
.col-head{font-size:14px;letter-spacing:.5px;color:var(--footer-dim)}
.col-body{font-size:10.4px;line-height:19.2px;letter-spacing:.6px;color:#7f859a}
.col-link{font-size:12px;letter-spacing:.4px;color:#8e94a8}
</style>
</head>
<body>
<div class="canvas">

  <div class="abs hero-strip">
    <div class="left" role="img" aria-label="Photo of a satellite dish frame in deep blue tones"></div>
    <div class="right" role="img" aria-label="Photo of an aerial mast against a blue sky"></div>
  </div>

  <section class="abs testimonials"></section>
  <h2 class="abs section-title">What Our <span class="accent">Customers</span> Think</h2>
  <svg class="abs quote-mark" width="36" height="28" viewBox="0 0 36 28" aria-hidden="true">
    <path d="M2 26V14C2 6 6 2 14 1v5c-4 1-6 3-6 7h6v13z" fill="var(--orange)"/>
    <path d="M20 26V14c0-8 4-12 12-13v5c-4 1-6 3-6 7h6v13z" fill="var(--orange)"/>
  </svg>
  <p class="abs quote-text">Lorem ipsum dolor sit amet, consetetur sadipscing elitr, sed diam nonumy eirmod tempor invidunt ut labore et dolore magna aliquyam erat, sed<br>diam voluptua. At vero eos et accusam et justo duo dolores et ea rebum. Stet clita kasd gubergren, no sea takimata sanctus est Lorem ipsum<br>dolor sit amet. Lorem ipsum dolor sit amet, consetetur sadipscing elitr</p>

  <div class="abs avatar" style="left:228px;top:260px" role="img" aria-label="Portrait photo of customer Helen Carrow"></div>
  <div class="abs person" style="left:341px;top:293px">&nbsp;Helen Carrow<br>Customer</div>

  <div class="abs avatar active" style="left:510px;top:264px" role="img" aria-label="Portrait photo of customer Owen Tarrant"></div>
  <div class="abs person" style="left:631px;top:295px">Owen Tarrant<br>&nbsp;Customer</div>

  <div class="abs avatar" style="left:790px;top:260px" role="img" aria-label="Portrait photo of customer Gordon Ashby"></div>
  <div class="abs person" style="left:893px;top:295px;line-height:19px">&nbsp;Gordon Ashby<br>Customer</div>

  <section class="abs contact"></section>
  <h2 class="abs contact-title">Contact Kestrel Mend &amp; Reach Today - For Same Day Service</h2>
  <h3 class="abs info-head">Company Information</h3>
  <p class="abs info-body" style="left:297px;top:531px;width:270px">Phone Kestrel Mend &amp; Reach now for a Free<br>Estimate and same day TV Aerial and Home<br>Satellite installations. Many of our other<br>services are also available at short notice</p>
  <p class="abs info-label" style="left:296px;top:629px">Our Opening Hours</p>
  <p class="abs info-body" style="left:296px;top:647px">8:00am - 8:00pm - Monday - Saturday</p>
  <p class="abs info-label" style="left:297px;top:696px">Our Payment Details</p>
  <p class="abs info-body" style="left:297px;top:713px;width:280px">We accept all major credit cards, and secure<br>payment can be made on-site, and on completion<br>of the work.</p>

  <div class="abs field" style="left:668px;top:525px;width:109px;height:25px">Name:</div>
  <div class="abs field" style="left:790px;top:525px;width:108px;height:25px">Last name:</div>
  <div class="abs field" style="left:668px;top:562px;width:230px;height:24px">Email:</div>
  <div class="abs field" style="left:668px;top:599px;width:230px;height:25px">Post code:</div>
  <div class="abs field" style="left:668px;top:638px;width:230px;height:78px">Your message:</div>
  <div class="abs send-btn">Send Message Now</div>

  <footer>
    <div class="abs footer-bar"></div>
    <svg class="abs" style="left:148px;top:848px" width="20" height="28" viewBox="0 0 20 28" aria-hidden="true">
      <path d="M10 1C5 1 1 5 1 10c0 7 9 17 9 17s9-10 9-17c0-5-4-9-9-9z" fill="#9096a6"/>
      <circle cx="10" cy="10" r="3.5" fill="var(--footer-top)"/>
    </svg>
    <p class="abs footer-text" style="left:196px;top:843px">Fennick Lane 114<br>Brookmere, BK 40217</p>

    <svg class="abs" style="left:513px;top:851px" width="25" height="25" viewBox="0 0 24 24" aria-hidden="true">
      <path d="M5 2l4 4-2 3c1 3 4 6 7 7l3-2 4 4-3 3C10 21 3 14 2 5z" fill="none" stroke="#9096a6" stroke-width="1.4" stroke-linejoin="round"/>
    </svg>
    <p class="abs footer-text" style="left:565px;top:842px">1-77-404--2291<br>info@KestrelMend&amp;Reach.com</p>

    <div class="abs social" style="left:905px;top:851px"></div>
    <div class="abs social" style="left:935px;top:851px"></div>
    <div class="abs social" style="left:966px;top:851px"></div>
    <div class="abs social" style="left:997px;top:851px"></div>

    <div class="abs footer-main" role="img" aria-label="Night view of the Earth from orbit with city lights"></div>

    <h4 class="abs col-head" style="left:193px;top:997px">About us</h4>
    <p class="abs col-body" style="left:122px;top:1025px;width:240px">Lorem ipsum dolor sit amet, consetetur<br>sadipscing elitr, sed diam nonumy eirmod<br>tempor invidunt ut labore et dolore magna<br>aliquyam erat, sed diam voluptua. At vero<br>eos et accusam et justo duo dolores et ea<br>rebum. Stet clita kasd gubergren, no sea<br>takimata sanctus est Lorem ipsum dolor sit</p>

    <h4 class="abs col-head" style="left:614px;top:1001px">Navigation</h4>
    <p class="abs col-link" style="left:561px;top:1034px">About us</p>
    <p class="abs col-link" style="left:561px;top:1058px">Satellite</p>
    <p class="abs col-link" style="left:561px;top:1082px">intergation</p>
    <p class="abs col-link" style="left:561px;top:1106px">Contact Us</p>
    <p class="abs col-link" style="left:684px;top:1034px">Aerials</p>
    <p class="abs col-link" style="left:684px;top:1058px">system</p>
    <p class="abs col-link" style="left:684px;top:1082px">Areas</p>

    <h4 class="abs col-head" style="left:925px;top:997px">Information</h4>
    <p class="abs col-link" style="left:935px;top:1029px">About Us</p>
    <p class="abs col-link" style="left:935px;top:1053px">Contact Us</p>
    <p class="abs col-link" style="left:935px;top:1077px">Privacy Policy</p>
    <p class="abs col-link" style="left:935px;top:1101px">Terms of Use</p>
    <p class="abs col-link" style="left:935px;top:1125px">Sitemap</p>
  </footer>

</div>
</body>
</html>
```